1200 x 150 pixel banner ad max size 200KB

Hi - I'm looking for an animated GIF to be used as an online digital banner advert.

The banner ad is to promote sales of gas cylinders from a world-leading manufacturer.

Headline 1: SLASH YOUR ADMINISTRATION COSTS BY 50%
Headline 2: If you're not happy with our service - we will give you your money back!
Headline 3 (if possible): FREE Regulator for all new customers/vessels

**The banner needs to really stand out of the page and reflect our company and brand - We exist to revolutionise ship safety, performance and crew welfare.**

The banner ad needs to include the product logo and company logo - both attached.

The blue colours in our logos are:
Dark Blue
Pantone 303
C100 M047 Y023 K079
R000 G031 B051
HTML 001F33

Light Blue
Pantone 2995
CO83 M001 Y000 K000
R080 G177 B234
HTML 05B1EA

Target Market(s)

Marine industry buyers - fleet managers, ship owners, technical purchasers, superintendants

Industry/Entity Type

Marine

Requirements
Must have
• Company colours, product and company logo

```html
<!DOCTYPE html>
<html lang="en">
<head>
<meta charset="utf-8">
<title>Slash Your Administration Costs by 50%</title>
<link href="https://fonts.googleapis.com/css2?family=Open+Sans:wght@700;800&display=swap" rel="stylesheet">
<style>
  :root {
    --navy: #001F33;
    --sky: #05B1EA;
    --brand-blue: #1B5FA8;
    --white: #FFFFFF;
    --offer-yellow: #FFF200;
  }
  html, body {
    margin: 0;
    padding: 0;
    overflow: hidden;
    background: var(--white);
  }
  .banner {
    position: relative;
    width: 1200px;
    height: 150px;
    background: var(--white);
    overflow: hidden;
    font-family: "Open Sans", Arial, sans-serif;
  }
  .banner__shapes {
    position: absolute;
    inset: 0;
  }
  .banner__headline {
    position: absolute;
    left: 0;
    width: 1200px;
    top: 24px;
    margin: 0;
    text-align: center;
    color: var(--white);
    font-weight: 700;
    text-transform: uppercase;
    line-height: 1;
  }
  .headline__main {
    display: block;
    font-size: 35px;
    letter-spacing: 0.2px;
  }
  .headline__offer {
    display: block;
    margin-top: 10px;
    font-size: 30px;
  }
  .headline__figure {
    color: var(--offer-yellow);
    font-size: 58px;
    font-weight: 800;
    margin-left: 8px;
    vertical-align: -6px;
  }
  .brand {
    position: absolute;
    display: flex;
    align-items: center;
    font-weight: 800;
    white-space: nowrap;
  }
  .brand--company {
    left: 0;
    width: 200px;
    justify-content: center;
    top: 65px;
    font-size: 15px;
    color: var(--brand-blue);
  }
  .brand--product {
    left: 1012px;
    top: 58px;
    font-size: 20px;
    color: var(--navy);
    gap: 8px;
  }
  .brand__mark {
    width: 28px;
    height: 28px;
    border-radius: 50%;
    background: var(--sky);
    flex: none;
  }
</style>
</head>
<body>
  <div class="banner">
    <svg class="banner__shapes" width="1200" height="150" viewBox="0 0 1200 150" aria-hidden="true">
      <polygon class="stripe stripe--left" points="193,0 214,0 267,150 246,150" fill="var(--sky)"/>
      <polygon class="panel" points="213,0 1004,0 949,150 266,150" fill="var(--navy)"/>
      <polygon class="stripe stripe--right" points="1003,0 1022,0 967,150 948,150" fill="var(--sky)"/>
    </svg>

    <div class="brand brand--company">Keelwright Marine</div>

    <h1 class="banner__headline">
      <span class="headline__main">Slash your administration costs</span>
      <span class="headline__offer">By<span class="headline__figure">50%</span></span>
    </h1>

    <div class="brand brand--product">
      <span class="brand__mark"></span>
      <span class="brand__name">QuickTankGas</span>
    </div>
  </div>
</body>
</html>
```